ZAMO needs a beautiful/corp web page

We are a pump an compressor repair facility in Alberta Canada. We love clean looks. white yellows greens blues. main page should involve conola fields, sun shine

Reason: i will be guaranteeing the project keep up the good work

Requirements
Must have
• open conola fields

```html
<!DOCTYPE html>
<html lang="en">
<head>
<meta charset="utf-8">
<title>ZAMO – Pump &amp; Compressor Repair, Alberta</title>
<link href="https://fonts.googleapis.com/css2?family=Lobster+Two:ital,wght@1,700&family=Open+Sans:ital,wght@0,400;0,600;0,700;1,400&display=swap" rel="stylesheet">
<style>
:root{
  --yellow:#eea700;
  --canola:#f2cf1d;
  --leaf:#6aa33a;
  --sky:#5aa7dd;
  --ink:#444;
  --muted:#8a8a8a;
  --card:#f5f5f5;
  --white:#fff;
}
*{box-sizing:border-box;margin:0;padding:0}
html,body{width:1200px;height:2256px;overflow:hidden}
body{position:relative;background:var(--white);font-family:"Open Sans",Arial,sans-serif;color:var(--ink)}
.abs{position:absolute}

/* header */
.site-header{left:0;top:0;width:1200px;height:129px;background:var(--white);border-top:2px solid #9a9a9a}
.brand{left:138px;top:48px;display:flex;align-items:center;gap:8px;font-weight:700;font-size:26px;color:#333;letter-spacing:1px}
.brand-mark{width:14px;height:14px;background:var(--yellow)}
.nav-item{top:0;height:102px;width:120px;margin-left:-60px;text-align:center;font-size:15px;color:#555;padding-top:40px}
.nav-item svg{display:block;margin:0 auto 10px;width:14px;height:14px;fill:#888}
.nav-item.active{background:var(--yellow);color:var(--white);width:89px;margin-left:-44px}
.nav-item.active svg{fill:var(--white)}

/* hero */
.hero{left:0;top:129px;width:1200px;height:453px;background:linear-gradient(#f0f0f0,#e8e8e8)}
.slider{left:183px;top:177px;width:831px;height:369px;background:var(--white);box-shadow:0 1px 4px rgba(0,0,0,.15)}
.slide-image{left:0;top:0;width:831px;height:285px;background:
  radial-gradient(circle at 82% 18%,#fff6c8 0,#ffe680 9%,rgba(255,230,128,0) 24%),
  linear-gradient(180deg,#8fc7ee 0%,#bfe0f5 38%,#f4d93a 44%,#f2cf1d 70%,#c9b019 86%,#6aa33a 100%)}
.slide-caption{left:6px;top:171px;width:788px;height:95px;background:rgba(40,40,40,.78);color:#eee;font-style:italic;font-size:15px;line-height:25px;padding:10px 20px}
.thumb{top:291px;height:69px;width:190px}

/* intro */
.intro-title{left:0;top:620px;width:1200px;text-align:center;font-family:"Lobster Two",cursive;font-style:italic;font-weight:700;font-size:34px;color:#4a4a4a}
.intro-title em{color:var(--yellow);font-style:italic}
.intro-sub{left:0;top:672px;width:1200px;text-align:center;font-style:italic;font-size:19px;color:var(--muted)}

/* cards */
.service{top:759px;width:234px;height:278px;background:var(--card);border-bottom:2px solid var(--yellow);text-align:center}
.service.raised{box-shadow:0 0 12px rgba(0,0,0,.12)}
.service svg{position:absolute;left:95px;top:22px;width:44px;height:44px}
.card-title{position:absolute;left:0;width:100%;font-weight:700;font-size:15px;color:#3a3a3a;letter-spacing:.3px}
.service .card-title{top:78px}
.card-text{position:absolute;left:18px;width:198px;font-size:13.5px;line-height:25px;color:#888}
.service .card-text{top:112px}
.btn{position:absolute;left:64px;top:228px;width:106px;height:28px;background:var(--yellow);color:var(--white);font-size:12px;font-style:italic;line-height:28px}

.section-rule{left:99px;width:999px;height:1px;border-top:2px dotted #ddd}
.section-title{left:0;width:1200px;text-align:center;font-family:"Lobster Two",cursive;font-style:italic;font-weight:700;font-size:25px;color:#4a4a4a}
.section-title span{background:var(--white);padding:0 18px}

/* works */
.work{top:1172px;width:234px;height:354px;background:var(--card);border-bottom:2px solid var(--yellow);text-align:center}
.work-image{position:absolute;left:0;top:0;width:234px;height:153px}
.work .card-title{top:173px}
.work .card-text{top:207px;font-style:italic}
.work-actions{position:absolute;left:75px;top:295px;display:flex;gap:12px}
.round{width:36px;height:36px;border-radius:50%;background:var(--yellow);display:flex;align-items:center;justify-content:center}

/* testimonial */
.avatar{left:162px;top:1637px;width:66px;height:64px;background:linear-gradient(#e6e6e6,#bdbdbd);border:1px solid #ddd}
.quote{left:258px;top:1630px;width:760px;font-style:italic;font-size:15px;line-height:32px;color:#888}
.quote-author{left:258px;top:1725px;font-style:italic;font-size:15px;color:var(--yellow)}
.dots{left:885px;top:1762px;display:flex;gap:10px}
.dots i{width:12px;height:12px;background:#e2e2e2}
.dots i.on{background:var(--yellow)}

/* footer */
.site-footer{left:0;top:1848px;width:1200px;height:408px;background:#eeeeee}
.foot-col{top:1888px;width:240px;font-size:13.5px;line-height:25px;color:#777}
.foot-col h4{font-size:15px;font-weight:700;color:#3a3a3a;margin-bottom:14px}
.foot-col a{color:var(--yellow);text-decoration:none;font-style:italic}
.photos{display:grid;grid-template-columns:repeat(3,54px);gap:6px}
.photos i{width:54px;height:52px;display:block}
.contact-row{display:flex;gap:12px;margin-bottom:12px;line-height:24px}
.contact-row svg{flex:none;margin-top:6px;width:11px;height:11px;fill:#888}
.foot-rule{left:99px;top:2175px;width:999px;border-top:2px dotted #ddd}
.copyright{left:99px;top:2192px;font-size:13.5px;line-height:22px;color:#777}
.copyright span{color:var(--yellow)}
.social{top:2200px;left:966px;display:flex;gap:16px}
.social i{width:24px;height:24px;border-radius:50%;background:#8a8a8a}
</style>
</head>
<body>

<header class="abs site-header">
  <div class="abs brand"><span class="brand-mark"></span>ZAMO</div>
  <nav>
    <div class="abs nav-item active" style="left:581px"><svg viewBox="0 0 14 14"><path d="M7 1 1 7h2v6h3V9h2v4h3V7h2z"/></svg>HOME</div>
    <div class="abs nav-item" style="left:687px"><svg viewBox="0 0 14 14"><path d="M1 4h3l1-2h4l1 2h3v8H1zM7 5a2.5 2.5 0 1 0 0 5 2.5 2.5 0 0 0 0-5z"/></svg>PRODUCTS</div>
    <div class="abs nav-item" style="left:811px"><svg viewBox="0 0 14 14"><path d="M1 2h12v2H1zm0 4h12v2H1zm0 4h12v2H1z"/></svg>SOLUTIONS</div>
    <div class="abs nav-item" style="left:921px"><svg viewBox="0 0 14 14"><circle cx="7" cy="4" r="3"/><path d="M1 13c0-4 3-5 6-5s6 1 6 5z"/></svg>ABOUT</div>
    <div class="abs nav-item" style="left:1023px"><svg viewBox="0 0 14 14"><path d="M1 3h12v1L7 8 1 4zm0 3 6 4 6-4v6H1z"/></svg>CONTACT</div>
  </nav>
</header>

<section class="abs hero"></section>
<div class="abs slider">
  <div class="abs slide-image" role="img" aria-label="Open canola field in full yellow bloom under a sunny Alberta sky"></div>
  <p class="abs slide-caption">From the canola fields to the shop floor, ZAMO keeps Alberta's pumps and compressors running. Fast diagnostics, honest quotes and certified rebuilds for farm, oilfield and industrial equipment across the province, all season long.</p>
  <div class="abs thumb" role="img" aria-label="Canola field at sunrise" style="left:8px;background:linear-gradient(#ffe7a0,#f2cf1d 55%,#6aa33a)"></div>
  <div class="abs thumb" role="img" aria-label="Blue centrifugal pump on the workbench" style="left:210px;background:linear-gradient(90deg,#3c6fc4,#b9c3cf)"></div>
  <div class="abs thumb" role="img" aria-label="Air compressor after rebuild" style="left:412px;background:linear-gradient(#e8e8e8,#c8262a 60%,#ededed)"></div>
  <div class="abs thumb" role="img" aria-label="Canola rows meeting blue sky" style="left:614px;width:208px;background:linear-gradient(#9fd0f0,#f4d93a 50%,#5f9a34)"></div>
</div>

<h1 class="abs intro-title">We are <em>ZAMO</em>, Alberta's pump &amp; compressor experts.</h1>
<p class="abs intro-sub">We repair, rebuild and service pumps and compressors. Your equipment is safe with us.</p>

<div class="abs service" style="left:99px">
  <svg viewBox="0 0 44 44" fill="#444"><circle cx="22" cy="22" r="8"/><path d="M22 2v8M22 34v8M2 22h8M34 22h8M8 8l6 6M30 30l6 6M8 36l6-6M30 14l6-6" stroke="#444" stroke-width="3"/></svg>
  <h3 class="card-title">PUMP REPAIR</h3>
  <p class="card-text">Centrifugal, submersible and transfer pumps diagnosed, rebuilt and tested in our shop...</p>
  <span class="btn">Read more</span>
</div>
<div class="abs service" style="left:354px">
  <svg viewBox="0 0 44 44" fill="none" stroke="#444" stroke-width="3"><rect x="4" y="6" width="36" height="32"/><path d="M4 16h36M4 27h36M16 6v32M28 6v32"/></svg>
  <h3 class="card-title">COMPRESSOR SERVICE</h3>
  <p class="card-text">Reciprocating and rotary screw compressors serviced on site or in our repair bay...</p>
  <span class="btn">Read more</span>
</div>
<div class="abs service raised" style="left:609px">
  <svg viewBox="0 0 44 44"><path d="M6 40 30 16" stroke="#444" stroke-width="5"/><path d="M34 4l2 5 5 2-5 2-2 5-2-5-5-2 5-2zM22 6l1 3 3 1-3 1-1 3-1-3-3-1 3-1z" fill="#444"/></svg>
  <h3 class="card-title">FIELD CALLS</h3>
  <p class="card-text">Our trucks reach farms, yards and plants across Alberta when a breakdown can't wait...</p>
  <span class="btn">Read more</span>
</div>
<div class="abs service" style="left:864px">
  <svg viewBox="0 0 44 44" fill="#444"><path d="M12 4h16l6 6v8H12z"/><rect x="4" y="20" width="36" height="14" rx="2"/><rect x="12" y="30" width="20" height="10" fill="#f5f5f5" stroke="#444" stroke-width="2"/></svg>
  <h3 class="card-title">PARTS &amp; REPORTS</h3>
  <p class="card-text">Genuine parts in stock and a written test report with every job we complete...</p>
  <span class="btn">Read more</span>
</div>

<div class="abs section-rule" style="top:1110px"></div>
<h2 class="abs section-title" style="top:1092px"><span>Our Latest Work</span></h2>

<div class="abs work" style="left:99px">
  <div class="work-image" role="img" aria-label="Irrigation pump beside a canola field" style="background:linear-gradient(180deg,#a7d4f2 0%,#f2cf1d 50%,#6aa33a 100%)"></div>
  <h3 class="card-title">IRRIGATION PUMP</h3>
  <p class="card-text">Full rebuild of a farm irrigation pump ahead of the canola growing season...</p>
  <div class="work-actions"><span class="round"><svg width="16" height="16" viewBox="0 0 16 16" fill="none" stroke="#fff" stroke-width="2.5"><circle cx="7" cy="7" r="4.5"/><path d="M10 10l4 4"/></svg></span><span class="round"><svg width="16" height="16" viewBox="0 0 16 16" fill="none" stroke="#fff" stroke-width="2.2"><path d="M6 10 10 6M5 8 3 10a2.5 2.5 0 0 0 3 3l2-2M11 8l2-2a2.5 2.5 0 0 0-3-3L8 5"/></svg></span></div>
</div>
<div class="abs work" style="left:354px">
  <div class="work-image" role="img" aria-label="Blue water pump on a test stand" style="background:radial-gradient(circle at 55% 45%,#3d8fd6 0,#cfe3f4 45%,#f7f9fc 75%)"></div>
  <h3 class="card-title">WATER TRANSFER</h3>
  <p class="card-text">New seals and impeller for a municipal water transfer pump in central Alberta...</p>
  <div class="work-actions"><span class="round"><svg width="16" height="16" viewBox="0 0 16 16" fill="none" stroke="#fff" stroke-width="2.5"><circle cx="7" cy="7" r="4.5"/><path d="M10 10l4 4"/></svg></span><span class="round"><svg width="16" height="16" viewBox="0 0 16 16" fill="none" stroke="#fff" stroke-width="2.2"><path d="M6 10 10 6M5 8 3 10a2.5 2.5 0 0 0 3 3l2-2M11 8l2-2a2.5 2.5 0 0 0-3-3L8 5"/></svg></span></div>
</div>
<div class="abs work" style="left:609px">
  <div class="work-image" role="img" aria-label="Red shop air compressor after service" style="background:linear-gradient(180deg,#f2f2f2 20%,#d43a34 60%,#efefef)"></div>
  <h3 class="card-title">SHOP COMPRESSOR</h3>
  <p class="card-text">Valve and motor service on an 80-gallon shop compressor for a grain co-op...</p>
  <div class="work-actions"><span class="round"><svg width="16" height="16" viewBox="0 0 16 16" fill="none" stroke="#fff" stroke-width="2.5"><circle cx="7" cy="7" r="4.5"/><path d="M10 10l4 4"/></svg></span><span class="round"><svg width="16" height="16" viewBox="0 0 16 16" fill="none" stroke="#fff" stroke-width="2.2"><path d="M6 10 10 6M5 8 3 10a2.5 2.5 0 0 0 3 3l2-2M11 8l2-2a2.5 2.5 0 0 0-3-3L8 5"/></svg></span></div>
</div>
<div class="abs work" style="left:864px">
  <div class="work-image" role="img" aria-label="Sunshine over rolling canola hills" style="background:radial-gradient(circle at 70% 25%,#fff6c8 0,#ffe680 12%,rgba(255,230,128,0) 30%),linear-gradient(180deg,#8fc7ee 0%,#f4d93a 55%,#5f9a34 100%)"></div>
  <h3 class="card-title">OILFIELD SCREW UNIT</h3>
  <p class="card-text">Airend overhaul on a rotary screw compressor serving a rural well site...</p>
  <div class="work-actions"><span class="round"><svg width="16" height="16" viewBox="0 0 16 16" fill="none" stroke="#fff" stroke-width="2.5"><circle cx="7" cy="7" r="4.5"/><path d="M10 10l4 4"/></svg></span><span class="round"><svg width="16" height="16" viewBox="0 0 16 16" fill="none" stroke="#fff" stroke-width="2.2"><path d="M6 10 10 6M5 8 3 10a2.5 2.5 0 0 0 3 3l2-2M11 8l2-2a2.5 2.5 0 0 0-3-3L8 5"/></svg></span></div>
</div>

<div class="abs section-rule" style="top:1576px"></div>
<h2 class="abs section-title" style="top:1558px"><span>Testimonials</span></h2>

<div class="abs avatar" role="img" aria-label="Client avatar"></div>
<p class="abs quote">"Our irrigation pump failed two days before seeding. ZAMO had a truck at the farm that afternoon, rebuilt it in their shop overnight and had water on the canola by morning. Friendly people, fair prices and work that lasts season after season..."</p>
<p class="abs quote-author">Dale Marchuk, prairiegrain.example</p>
<div class="abs dots"><i class="on"></i><i></i><i></i><i></i></div>

<footer class="abs site-footer"></footer>
<div class="abs foot-col" style="left:99px">
  <h4>ABOUT US</h4>
  <p>ZAMO is a family-run pump and compressor repair facility in Alberta, Canada. For years we have kept farms, oilfield sites and municipal plants running with careful work, honest advice and quick turnaround.</p>
  <p style="margin-top:12px"><a>Read more...</a></p>
</div>
<div class="abs foot-col" style="left:354px">
  <h4>LATEST TWEETS</h4>
  <p>loading ...</p>
</div>
<div class="abs foot-col" style="left:609px">
  <h4>FLICKR PHOTOS</h4>
  <div class="photos" role="img" aria-label="Grid of shop and canola field photos">
    <i style="background:#f2cf1d"></i><i style="background:#6aa33a"></i><i style="background:#8fc7ee"></i>
    <i style="background:#d43a34"></i><i style="background:#e2b91a"></i><i style="background:#3c6fc4"></i>
    <i style="background:#5f9a34"></i><i style="background:#7a7a7a"></i>
  </div>
</div>
<div class="abs foot-col" style="left:864px">
  <h4>CONTACT US</h4>
  <div class="contact-row"><svg viewBox="0 0 12 12"><path d="M6 0a4 4 0 0 0-4 4c0 3 4 8 4 8s4-5 4-8a4 4 0 0 0-4-4zm0 5.5A1.5 1.5 0 1 1 6 2.5a1.5 1.5 0 0 1 0 3z"/></svg><span>Address: 4120 Range Road 22, Red Deer County, AB, Canada</span></div>
  <div class="contact-row"><svg viewBox="0 0 12 12"><path d="M2 0h3l1 3-2 1a7 7 0 0 0 4 4l1-2 3 1v3c0 1-1 2-2 2C5 12 0 7 0 2 0 1 1 0 2 0z"/></svg><span>Phone: +1 403 555 0142</span></div>
  <div class="contact-row"><svg viewBox="0 0 12 12"><circle cx="6" cy="3" r="3"/><path d="M0 12c0-4 3-5 6-5s6 1 6 5z"/></svg><span>Skype: Zamo_Repair</span></div>
  <div class="contact-row"><svg viewBox="0 0 12 12"><path d="M0 2h12v1L6 7 0 3zm0 3 6 4 6-4v5H0z"/></svg><span>Email: <a style="font-style:normal">service@zamo.example</a></span></div>
</div>
<div class="abs foot-rule"></div>
<p class="abs copyright">Copyright 2012 Zamo Pump &amp; Compressor - All rights reserved. Template<br>by <span>Kestrel</span>.</p>
<div class="abs social"><i></i><i></i><i></i><i></i></div>

</body>
</html>
```